Webdesign für Immobilienmanagement
Zielgruppe
Immobilienmanagement Unternehmen / allg. Hausverwaltung , Hausmeisterservice, Grünanlagenpflege, Unterhaltsreinigung, Winterdienst
Zielgruppe: Mieter und Wohnungseigentümer
Aufgabenstellung
Farben: weiß/grün
keine Kopie der alten Seite
nutzerfreundliche Unternehmenswebseite
Logo vorhanden auf alter Webseite

```html
<!DOCTYPE html>
<html lang="de">
<head>
<meta charset="utf-8">
<title>Hofmark Immobilien-Management GmbH</title>
<link rel="stylesheet" href="https://fonts.googleapis.com/css2?family=Michroma&family=Arimo:wght@400;700&display=swap">
<style>
  :root {
    --green: #4cb034;
    --ink: #222222;
    --muted: #444444;
    --alert: #e02020;
    --page: #ffffff;
    --hero-a: #e9e3da;
    --hero-b: #c7ab86;
    --hero-c: #f1ede6;
    --team-a: #e7e9ec;
    --team-b: #b9c2cc;
  }
  * { box-sizing: border-box; margin: 0; padding: 0; }
  html, body { width: 1200px; height: 1200px; overflow: hidden; background: var(--page); }
  body { font-family: "Arimo", Arial, sans-serif; color: var(--ink); position: relative; }

  .site-header { position: absolute; top: 0; left: 0; width: 1200px; height: 100px; }
  .meta-links { position: absolute; left: 222px; top: 28px; display: flex; gap: 14px; font-size: 11px; color: var(--muted); }
  .brand { position: absolute; left: 400px; top: 40px; width: 400px; text-align: center; font-size: 15px; font-weight: 700; color: var(--ink); letter-spacing: .2px; }
  .emergency { position: absolute; left: 916px; top: 28px; width: 60px; text-align: center; color: var(--alert); font-size: 7.5px; font-weight: 700; line-height: 1.1; }
  .emergency svg { display: block; margin: 0 auto 4px; }

  .header-rule { position: absolute; top: 100px; left: 0; width: 1200px; height: 3px; background: var(--green); }

  .main-nav { position: absolute; top: 103px; left: 0; width: 1200px; height: 67px; }
  .main-nav a { position: absolute; top: 24px; font-size: 14px; font-weight: 700; color: var(--ink); text-decoration: none; letter-spacing: .2px; }
  .main-nav .nav-contact { top: 15px; background: var(--green); color: #fff; padding: 9px 17px; border-radius: 18px; }

  .hero { position: absolute; top: 170px; left: 0; width: 1200px; height: 480px;
    background: linear-gradient(100deg, var(--hero-c) 0%, var(--hero-a) 30%, var(--hero-b) 55%, var(--hero-a) 75%, #d8dcd0 100%); }
  .hero-title { position: absolute; left: 222px; top: 60px; font-family: "Michroma", sans-serif; font-size: 28px; line-height: 1.3; color: #2b2b2b; }
  .hero-cta { position: absolute; left: 222px; top: 160px; background: var(--green); color: #fff; font-weight: 700; font-size: 14px; padding: 10px 20px; border-radius: 20px; }
  .hero-dots { position: absolute; left: 570px; bottom: 30px; display: flex; gap: 7px; }
  .hero-dots span { width: 12px; height: 12px; border: 1.5px solid #fff; border-radius: 50%; }
  .hero-dots span.active { background: #fff; }

  .section-title { font-family: "Michroma", sans-serif; font-size: 13px; color: var(--ink); letter-spacing: .3px; }

  .services { position: absolute; top: 690px; left: 222px; width: 760px; }
  .service-list { display: flex; justify-content: space-between; margin-top: 26px; }
  .service { display: flex; align-items: center; gap: 6px; font-family: "Michroma", sans-serif; font-size: 6.5px; line-height: 1.25; color: var(--ink); }
  .service svg { flex: none; stroke: var(--green); fill: none; stroke-width: 1.4; stroke-linecap: round; stroke-linejoin: round; }

  .team { position: absolute; top: 800px; left: 222px; width: 760px; }
  .team-photo { position: absolute; top: 40px; left: 0; width: 180px; height: 150px; background: linear-gradient(135deg, var(--team-a), var(--team-b)); }
  .team-text { position: absolute; top: 52px; left: 198px; width: 380px; font-size: 11.5px; line-height: 1.55; color: #333; }
  .team-text p + p { margin-top: 14px; }

  .hours { position: absolute; top: 800px; left: 897px; width: 110px; font-size: 8.5px; color: #333; line-height: 1.3; }
  .hours h3 { font-size: 8.5px; font-weight: 700; margin-bottom: 14px; }
  .hours dt { font-weight: 700; margin-top: 10px; }
  .hours .note { font-size: 5.5px; margin-top: 16px; line-height: 1.5; color: #555; }
</style>
</head>
<body>
  <header class="site-header">
    <nav class="meta-links"><span>Partnerlinks</span><span>Impressum</span><span>Datenschutz</span></nav>
    <div class="brand">Hofmark Immobilien-Management GmbH</div>
    <div class="emergency">
      <svg width="40" height="30" viewBox="0 0 40 30">
        <g stroke="#e02020" stroke-width="1.6" stroke-linecap="round">
          <line x1="20" y1="1" x2="20" y2="5"/><line x1="9" y1="5" x2="12" y2="8"/><line x1="31" y1="5" x2="28" y2="8"/>
          <line x1="4" y1="14" x2="8" y2="14"/><line x1="32" y1="14" x2="36" y2="14"/>
        </g>
        <path d="M13 24 V17 a7 7 0 0 1 14 0 V24 Z" fill="#e02020"/>
        <rect x="10" y="24" width="20" height="4" fill="#e02020"/>
        <rect x="19" y="13" width="2" height="6" fill="#fff"/><rect x="19" y="20.5" width="2" height="2" fill="#fff"/>
      </svg>
      24-STUNDEN<br>NOTDIENST
    </div>
  </header>
  <div class="header-rule"></div>

  <nav class="main-nav">
    <a style="left:370px">Über uns</a>
    <a style="left:479px">Hausverwaltung</a>
    <a style="left:630px">Hausmeister</a>
    <a style="left:758px">Downloads</a>
    <a class="nav-contact" style="left:893px">Kontakt</a>
  </nav>

  <section class="hero" role="img" aria-label="Foto: Familie mit Kindern beim Einzug, Umzugskartons im Wohnzimmer">
    <h1 class="hero-title">UNSER NEUES<br>ZUHASE!</h1>
    <div class="hero-cta">Mietwohnungen entdecken</div>
    <div class="hero-dots"><span class="active"></span><span></span><span></span><span></span></div>
  </section>

  <section class="services">
    <h2 class="section-title">UNSERE LEISTUNGEN</h2>
    <div class="service-list">
      <div class="service">
        <svg width="20" height="20" viewBox="0 0 20 20"><path d="M2 10 L10 3 L18 10"/><path d="M4 9 V18 H16 V9"/><rect x="7" y="11" width="6" height="5"/><line x1="10" y1="11" x2="10" y2="16"/><line x1="7" y1="13.5" x2="13" y2="13.5"/></svg>
        <span>ALLGEMEINE<br>HAUSVERWALTUNG</span>
      </div>
      <div class="service">
        <svg width="22" height="20" viewBox="0 0 22 20"><path d="M1 8 L5 6 L10 8 L13 6 L21 8"/><path d="M5 6 L3 12 L8 16 L14 13 L19 11"/><path d="M9 11 L12 13.5 M11 9.5 L14 12"/></svg>
        <span>KAUFMÄNNISCHE<br>BETREUUNG</span>
      </div>
      <div class="service">
        <svg width="20" height="20" viewBox="0 0 20 20"><circle cx="10" cy="10" r="8"/><circle cx="10" cy="10" r="5"/><circle cx="10" cy="10" r="2"/></svg>
        <span>TECHNISCHE<br>BETREUUNG</span>
      </div>
      <div class="service">
        <svg width="20" height="20" viewBox="0 0 20 20"><line x1="3" y1="17" x2="15" y2="5"/><path d="M13 3 a3 3 0 0 0 4 4"/><line x1="3" y1="3" x2="17" y2="17"/><path d="M2 5 L5 2"/></svg>
        <span>HAUSMEISTER<br>SERVICE</span>
      </div>
      <div class="service">
        <svg width="20" height="20" viewBox="0 0 20 20"><path d="M5 11 H15 L14 18 H6 Z"/><path d="M10 11 V4 M10 7 Q6 5 5 2 M10 6 Q14 4 15 1"/></svg>
        <span>GRÜNANLAGEN<br>PFLEGE</span>
      </div>
      <div class="service">
        <svg width="20" height="20" viewBox="0 0 20 20"><line x1="6" y1="2" x2="6" y2="14"/><path d="M3 14 H9 L10 18 H2 Z"/><rect x="12" y="9" width="6" height="9"/><path d="M14 9 V6 H16"/></svg>
        <span>UNTERHALTS<br>REINIGUNG</span>
      </div>
      <div class="service">
        <svg width="20" height="20" viewBox="0 0 20 20"><line x1="10" y1="1" x2="10" y2="19"/><line x1="2" y1="5.5" x2="18" y2="14.5"/><line x1="2" y1="14.5" x2="18" y2="5.5"/><path d="M8 2.5 L10 4.5 L12 2.5 M8 17.5 L10 15.5 L12 17.5"/></svg>
        <span>WINTER<br>DIENST</span>
      </div>
    </div>
  </section>

  <section class="team">
    <h2 class="section-title">UNSER TEAM</h2>
    <div class="team-photo" role="img" aria-label="Foto: Team des Unternehmens, drei Personen im Büro"></div>
    <div class="team-text">
      <p>Wir sind ein junges, freundliches, gut ausgebildetes Team, das sich mit all seiner Aufmerksamkeit und Kompetenz um Ihre Wünsche in Sachen Immobilien kümmert. Möchten Sie eine Wohnung mieten, suchen Sie einen Hausmeister … oder einen Verwalter für Ihre Immobilie?</p>
      <p>Schauen Sie sich unser Leistungsangebot an und überzeugen Sie sich selbst von den Vorteilen, die wir Ihnen bieten können.</p>
    </div>
  </section>

  <aside class="hours">
    <h3>Unsere<br>Geschäftszeiten:</h3>
    <dl>
      <dt>Montag</dt><dd>09:00–12:00 Uhr</dd>
      <dt>Dienstag</dt><dd>09:00–12:00 Uhr<br>13:00–15:00 Uhr</dd>
      <dt>Donnerstag</dt><dd>09:00–12:00 Uhr<br>13:00–18:00 Uhr</dd>
    </dl>
    <p class="note">Termine außerhalb der Geschäftszeiten nach Vereinbarung möglich.</p>
  </aside>
</body>
</html>
```